Plumwick website

Provide a website for a business that is an online farmstand for mostly organic farm products produced on our 9 farms and packaged at our mill. We will be targeting an urban and suburban audience that will be able know the farms where their food is grown and "pick" their food online. We want the site to feel to feel fresh and urbane. Winning logo attached.

The website will feature:

A section with descriptions, pictures and Google maps for the farms as well as the produce produced on each farm. We will want to establish a provenance to the mostly organic food we produce and sell - and visit the farms if they want. We want our customers to know where their food comes from without having to live on a farm. We will market products of local farmers in addition to our own. We'll need room for about 50 farm descriptions and about 5 product descriptions per farm.

A master growing schedule -- there should be room for about 5 products per farm.

An online store (maybe linked to the farm and product) descriptions

An about us section -- where we can tell our family's story and about the history of the mill where we package food and provide fulfillment

A section for links to other farming and food information

A section for legal notices
Updates

Project Deadline Extended
Reason: Holiday weekend for many in USA

Target Market(s)

Educated, urban market who wants quality food at fair prices.

Industry/Entity Type

Farm

```html
<!DOCTYPE html>
<html lang="en">
<head>
<meta charset="utf-8">
<title>Plumwick – Steady growth for your farm</title>
<link href="https://fonts.googleapis.com/css2?family=Alegreya:wght@400;700&family=Arimo:wght@400;700&display=swap" rel="stylesheet">
<style>
:root{
  --green:#7cc144;
  --green-dark:#5e9b2c;
  --green-text:#7bb43a;
  --ink:#555;
  --muted:#777;
  --paper:#f3f3f3;
  --white:#fff;
  --topbar:#f0f0f0;
  --footer:#2f2f2f;
  --price:#c0282d;
  --btn:#666;
}
*{box-sizing:border-box;margin:0;padding:0}
html,body{width:735px;height:1200px;overflow:hidden}
body{position:relative;background:var(--paper);font-family:"Arimo",Arial,sans-serif;color:var(--ink)}

/* top bar */
.topbar{position:absolute;left:0;top:0;width:735px;height:33px;background:var(--topbar);border-bottom:1px solid #e2e2e2}
.topbar .links{position:absolute;left:95px;top:10px;font-size:7.5px;color:var(--muted)}
.topbar .links span{margin-right:14px}
.topbar .auth{position:absolute;left:277px;top:1px;display:flex;gap:4px}
.topbar .auth span{background:var(--green);color:var(--white);font-size:7.5px;padding:3px 8px;border-radius:2px;border:1px solid var(--green-dark)}
.topbar .social{position:absolute;right:93px;top:6px;display:flex;gap:6px}
.topbar .social span{width:14px;height:14px;border-radius:50%;border:1px solid #9a9a9a;display:block}

/* header */
.header{position:absolute;left:0;top:33px;width:735px;height:44px;background:var(--white)}
.brand{position:absolute;left:96px;top:7px;display:flex;align-items:center;gap:5px}
.brand .mark{width:12px;height:12px;background:var(--green)}
.brand .name{font-family:"Alegreya",Georgia,serif;font-size:17px;color:var(--green-text);letter-spacing:1px;font-weight:700}
.cart-note{position:absolute;left:96px;top:29px;font-size:7px;color:var(--muted)}
.nav{position:absolute;left:253px;top:8px;display:flex;gap:22px;font-family:"Alegreya",Georgia,serif;font-size:9.5px;color:var(--muted)}
.nav .active{color:var(--green-text);position:relative}
.nav .active::after{content:"";position:absolute;left:-6px;right:-6px;bottom:-6px;height:1px;background:var(--green)}

/* hero */
.hero{position:absolute;left:0;top:77px;width:735px;height:294px;
  background:
    radial-gradient(ellipse at 38% 30%,rgba(255,255,220,.95) 0,rgba(240,245,150,.6) 22%,rgba(240,245,150,0) 50%),
    linear-gradient(180deg,#d7e86a 0,#bcd84e 40%,#8fc23a 62%,#6fae2c 100%)}
.hero h1{position:absolute;left:0;width:735px;top:106px;text-align:center;font-family:"Alegreya",Georgia,serif;font-weight:400;font-size:37px;letter-spacing:1.5px;color:var(--white);text-shadow:0 1px 3px rgba(90,110,20,.35)}
.hero-arrow{position:absolute;top:134px;width:24px;height:30px;background:#333}
.hero-arrow.left{left:0}.hero-arrow.right{right:0}
.hero-arrow svg{position:absolute;left:7px;top:9px}

/* features */
.features{position:absolute;left:85px;top:327px;width:565px;display:flex;justify-content:space-between}
.feature{width:140px;text-align:center}
.feature .photo{width:124px;height:124px;margin:0 auto;border-radius:50%;border:6px solid var(--white);box-shadow:0 3px 4px rgba(0,0,0,.25)}
.feature h3{margin-top:22px;font-family:"Alegreya",Georgia,serif;font-weight:400;font-size:16.5px;color:var(--ink)}
.feature .rule{width:54px;height:1px;background:#ccc;margin:10px auto 16px}
.feature p{font-size:7px;line-height:10px;color:var(--muted);padding:0 8px;height:32px}
.btn-more{display:inline-block;margin-top:10px;background:var(--btn);color:var(--white);font-size:7px;padding:4px 8px;border:1px solid #444}
.photo.veg{background:radial-gradient(circle at 40% 40%,#f2c046,#c84b2a 55%,#5b8a2f)}
.photo.greens{background:radial-gradient(circle at 50% 60%,#c63a2b 0,#3f7d2a 45%,#1f4f1a)}
.photo.seeds{background:radial-gradient(circle at 50% 45%,#d65a7a,#8e2640 55%,#3d6b24)}
.photo.sprout{background:radial-gradient(circle at 50% 50%,#b8e27b,#4f9a2e 60%,#1e5d1b)}

/* clients */
.clients{position:absolute;left:0;top:610px;width:735px;height:301px;background:var(--green)}
.clients h2{position:absolute;top:12px;width:735px;text-align:center;font-family:"Alegreya",Georgia,serif;font-weight:400;font-size:25px;color:var(--white)}
.clients .sub{position:absolute;top:44px;width:735px;text-align:center;font-size:10px;color:var(--white)}
.clients .rule{position:absolute;left:250px;top:69px;width:258px;height:1px;background:rgba(255,255,255,.55)}
.client-names{position:absolute;left:115px;top:97px;width:500px;display:flex;justify-content:space-between;align-items:center}
.client-names span{font-weight:700;font-size:21px;color:var(--white);display:flex;align-items:center;gap:6px}
.client-names i{display:block;width:12px;height:12px;border-radius:50%;background:var(--white)}
.carousel{position:absolute;left:190px;top:145px;width:355px;height:146px;background:var(--white);border-radius:3px}
.car-arrow{position:absolute;top:204px;width:18px;height:18px;border-radius:50%;background:#4d7c2b}
.car-arrow.left{left:163px}.car-arrow.right{left:549px}
.car-arrow svg{position:absolute;left:5px;top:5px}
.products{position:absolute;left:5px;top:4px;display:flex;gap:11px}
.product{width:78px;text-align:center}
.product .shot{width:78px;height:80px;border:1px solid #ddd;background:radial-gradient(ellipse 30% 42% at 50% 58%,#c9307e 0,#e59cc4 70%,rgba(255,255,255,0) 100%),#fafafa}
.product .price{margin-top:5px;font-size:7px;color:var(--ink)}
.product .price b{color:var(--price)}
.product .pname{margin-top:6px;font-size:7px;color:var(--green-text);font-weight:700}
.product .cta{display:block;margin:3px auto 0;width:48px;font-size:6.5px;border:1px solid #999;background:#f0f0f0;padding:1px 0;color:#222}

/* community */
.community h2{position:absolute;left:95px;top:925px;font-family:"Alegreya",Georgia,serif;font-weight:400;font-size:24px;color:var(--ink)}
.globe{position:absolute;left:115px;top:963px;width:112px;height:112px;border-radius:50%;background:radial-gradient(circle at 45% 45%,#e8f7c4,#8fd14a 50%,#3f8e22 100%)}
.community-text{position:absolute;left:255px;top:963px;width:220px}
.community-text .lead{font-size:9px;line-height:12px;color:var(--ink)}
.community-text .body{margin-top:6px;font-size:6.5px;line-height:10px;color:var(--muted)}
.values{margin-top:18px;display:grid;grid-template-columns:110px 110px;row-gap:10px}
.values h4{font-size:7px;color:var(--green-text);letter-spacing:.3px}
.values p{font-size:6.5px;line-height:9.5px;color:var(--muted);margin-top:3px}
.members{position:absolute;left:488px;top:923px;width:152px;height:131px;border:1px solid #ddd;background:#f8f8f8}
.members h3{padding:6px 0 0 8px;font-family:"Alegreya",Georgia,serif;font-weight:400;font-size:23px;color:var(--ink)}
.member{display:flex;align-items:center;gap:8px;margin:6px 0 0 12px}
.member .avatar{width:24px;height:24px}
.member .avatar.a{background:linear-gradient(135deg,#8a2a22,#c9543f)}
.member .avatar.b{background:linear-gradient(135deg,#30507a,#e3823a)}
.member span{font-size:7px;font-weight:700;color:var(--green-text)}
.members-link{position:absolute;left:488px;top:1065px;width:152px;text-align:center;font-size:7px;color:var(--green-text)}

/* footer */
.footer{position:absolute;left:0;top:1160px;width:735px;height:40px;background:var(--footer)}
.footer p{position:absolute;left:95px;top:12px;font-size:6.5px;color:#8a8a8a}
.footer .top-link{position:absolute;left:624px;top:10px;width:17px;height:17px;border-radius:50%;border:1px solid #777}
.footer .top-link svg{position:absolute;left:4px;top:4px}
</style>
</head>
<body>

<div class="topbar">
  <div class="links"><span>About Us</span><span>Notices</span><span>Information</span></div>
  <div class="auth"><span>Log in &#9662;</span><span>Register</span></div>
  <div class="social"><span></span><span></span><span></span><span></span></div>
</div>

<header class="header">
  <div class="brand"><span class="mark"></span><span class="name">PLUMWICK</span></div>
  <div class="cart-note">Shopping Cart Empty</div>
  <nav class="nav"><span class="active">Home</span><span>Community</span><span>Store</span><span>Gallery</span><span>Contact Us</span></nav>
</header>

<section class="hero" role="img" aria-label="Sunny green meadow with a fruit tree, a basket of glowing produce, rabbits and daisies">
  <h1>STEADY GROWTH FOR YOUR FARM!</h1>
  <div class="hero-arrow left"><svg width="10" height="12"><path d="M8 1 L2 6 L8 11" stroke="#fff" stroke-width="1.5" fill="none"/></svg></div>
  <div class="hero-arrow right"><svg width="10" height="12"><path d="M2 1 L8 6 L2 11" stroke="#fff" stroke-width="1.5" fill="none"/></svg></div>
</section>

<section class="features">
  <div class="feature">
    <div class="photo veg" role="img" aria-label="Assorted fresh vegetables"></div>
    <h3>Premium products</h3><div class="rule"></div>
    <p>Lorem ipsum dolor sit amet consect etuer adipiscing elit diam nonummy nibh euismod.</p>
    <span class="btn-more">READMORE...</span>
  </div>
  <div class="feature">
    <div class="photo greens" role="img" aria-label="Leafy greens with a red pepper"></div>
    <h3>Advanced traits</h3><div class="rule"></div>
    <p>Ut wisi enim ad minim veniam quis nostrud exerci tation ullamcorper suscipit lobortis.</p>
    <span class="btn-more">READMORE...</span>
  </div>
  <div class="feature">
    <div class="photo seeds" role="img" aria-label="Pink speckled beans"></div>
    <h3>Agricultural seeds</h3><div class="rule"></div>
    <p>Duis autem vel eum iriure dolor in hendrerit in vulputate velit esse molestie.</p>
    <span class="btn-more">READMORE...</span>
  </div>
  <div class="feature">
    <div class="photo sprout" role="img" aria-label="Young seedling sprouting from soil"></div>
    <h3>Our technologies</h3><div class="rule"></div>
    <p>Nam liber tempor cum soluta nobis eleifend option congue nihil imperdiet doming quod.</p>
    <span class="btn-more">READMORE...</span>
  </div>
</section>

<section class="clients">
  <h2>Our awesome clients</h2>
  <div class="sub">When quality matters to you and your customer</div>
  <div class="rule"></div>
  <div class="client-names">
    <span><i></i>Greenleaf</span>
    <span>Fieldlab</span>
    <span>Sunvolt</span>
    <span>Norwick</span>
  </div>
  <div class="car-arrow left"><svg width="8" height="8"><path d="M6 0 L2 4 L6 8" stroke="#fff" stroke-width="1.5" fill="none"/></svg></div>
  <div class="carousel">
    <div class="products">
      <div class="product"><div class="shot" role="img" aria-label="Pink product bottle"></div><div class="price"><b>$26.00</b> each</div><div class="pname">Product 1</div><span class="cta">Add to cart</span><span class="cta">Add to wishlist</span></div>
      <div class="product"><div class="shot" role="img" aria-label="Pink product bottle"></div><div class="price"><b>$26.00</b> each</div><div class="pname">Product 1</div><span class="cta">Add to cart</span><span class="cta">Add to wishlist</span></div>
      <div class="product"><div class="shot" role="img" aria-label="Pink product bottle"></div><div class="price"><b>$26.00</b> each</div><div class="pname">Product 1</div><span class="cta">Add to cart</span><span class="cta">Add to wishlist</span></div>
      <div class="product"><div class="shot" role="img" aria-label="Pink product bottle"></div><div class="price"><b>$26.00</b> each</div><div class="pname">Product 1</div><span class="cta">Add to cart</span><span class="cta">Add to wishlist</span></div>
    </div>
  </div>
  <div class="car-arrow right"><svg width="8" height="8"><path d="M2 0 L6 4 L2 8" stroke="#fff" stroke-width="1.5" fill="none"/></svg></div>
</section>

<section class="community">
  <h2>Online Farm Community</h2>
  <div class="globe" role="img" aria-label="Green globe wrapped in leaves"></div>
  <div class="community-text">
    <p class="lead">Our offers a perfect base to present your information and emotions in a stunning manner.</p>
    <p class="body">Loremipsum is simply dummy text of the printing and typesetting industry. Loremipsum has been the industry's standard dummy text ever since the 1500s, when an unknown printer took a galley of type and scrambled it to make a type specimen book.</p>
    <div class="values">
      <div><h4>INTEGRITY</h4><p>Phasellus turpis orci, gravidapel dolor lentesque adipiscing.</p></div>
      <div><h4>SHARING</h4><p>Phasellus turpis orci, gravidapel dolor lentesque adipiscing.</p></div>
      <div><h4>DIALOGUE</h4><p>Phasellus turpis orci, gravidapel dolor lentesque adipiscing.</p></div>
      <div><h4>TRANSPARENCY</h4><p>Phasellus turpis orci, gravidapel dolor lentesque adipiscing.</p></div>
    </div>
  </div>
  <aside class="members">
    <h3>Members</h3>
    <div class="member"><div class="avatar a" role="img" aria-label="Member avatar"></div><span>mike</span></div>
    <div class="member"><div class="avatar b" role="img" aria-label="Member avatar"></div><span>Super User</span></div>
  </aside>
  <div class="members-link">View Members-Plumwick Community</div>
</section>

<footer class="footer">
  <p>Copyright © 2013 Plumwick Farms Community. All Rights Reserved.</p>
  <div class="top-link"><svg width="8" height="8"><path d="M0 6 L4 2 L8 6" stroke="#999" stroke-width="1.2" fill="none"/></svg></div>
</footer>

</body>
</html>
```